Keystrel Environmental and Regulatory - Summary of Services

Looking for a 3 (plus nice title page) brochure to advertise our various services for business (Keystrel Environmental and Regulatory Inc) in the environmental and regulatory field for oil and gas clients based in Alberta Canada. We complete environmental assessments in the field to ensure the environment is protected, emissions modelling and carbon emissions modelling, along with managing regulatory requirements for oil and gas. I'm hoping to have various services and lists along with graphics that relate to that area. We want to cater towards a business that is strong, but has green ideals. I've attached the Land Renewal Initiative brochure as an example of services, as well as our original Keystrel Brochure. I'd like to blend these two together for more of a modern feel with graphics overlay and condense to 3 pages (Title Page) for a more summary feel of this work.
Updates

Our website is Has lots of photos and the services on the website tab is what services we'd like to add to brochure. www.keystrelenvironmental.example

```html
<!DOCTYPE html>
<html lang="en">
<head>
<meta charset="utf-8">
<title>Keystrel Environmental and Regulatory – Services Brochure</title>
<link rel="stylesheet" href="https://fonts.googleapis.com/css2?family=Ubuntu:wght@300;400;500;700&family=Source+Sans+3:wght@400;600&display=swap">
<style>
  :root{
    --paper:#dedede;
    --forest:#1d4038;
    --forest-deep:#163a31;
    --navy:#0f2637;
    --navy-light:#1c3a4e;
    --leaf:#43c25a;
    --teal-green:#2b8f66;
    --heading:#1d4a3f;
    --ink:#1b1b1b;
    --white:#ffffff;
    --caption-band:#0f2333;
  }
  *{box-sizing:border-box;margin:0;padding:0}
  html,body{width:1200px;height:849px;overflow:hidden;background:var(--paper)}
  .spread{position:relative;width:1200px;height:849px;background:var(--paper);font-family:"Source Sans 3",sans-serif;color:var(--ink)}
  .abs{position:absolute}
  .fold{left:585px;top:0;width:30px;height:849px;background:linear-gradient(90deg,rgba(0,0,0,0) 0%,rgba(0,0,0,.07) 60%,rgba(0,0,0,.16) 100%)}

  /* photos */
  .photo-field{left:41px;top:0;width:165px;height:270px;background:linear-gradient(180deg,#7e95ad 0%,#a9b7c4 30%,#6d655c 42%,#5b4f45 100%)}
  .photo-canola{left:607px;top:548px;width:280px;height:212px;background:linear-gradient(180deg,#6f7f50 0%,#c9c23a 22%,#e4dc2f 60%,#d4cd25 100%)}
  .caption{font-family:"Ubuntu",sans-serif;font-size:5.6px;line-height:8.8px;color:var(--white)}
  .caption dt{float:left;width:42px;font-weight:700;clear:left}
  .caption dd{margin-left:42px}
  .caption-field{left:41px;top:270px;width:165px;height:38px;background:var(--teal-green);background:#22634c;padding:6px 0 0 13px}
  .caption-canola{left:607px;top:760px;width:280px;height:45px;background:var(--caption-band);padding:8px 0 0 13px}
  .caption-canola dt{width:47px}
  .caption-canola dd{margin-left:47px}

  /* section titles */
  .section-title{font-family:"Ubuntu",sans-serif;font-weight:700;font-size:16.5px;letter-spacing:.2px}
  .values-title{left:229px;top:50px;height:24px;border-left:2px solid var(--heading);padding-left:14px;color:var(--heading);line-height:24px}
  .icon-sprout{left:852px;top:54px;width:26px;height:27px}
  .values-quote{left:229px;top:100px;font-family:"Ubuntu",sans-serif;font-weight:300;font-size:18px;color:var(--leaf);white-space:nowrap}

  .mission{left:229px;top:163px;width:250px;font-family:"Ubuntu",sans-serif}
  .mission h2{font-size:14.5px;font-weight:700;color:var(--heading);margin-bottom:9px}
  .mission p{font-size:14.3px;font-weight:300;color:var(--teal-green);line-height:17.5px;margin-bottom:8px}

  .values-body{left:495px;top:152px;width:383px;font-size:8.3px;line-height:11.2px;text-align:justify}
  .values-body p{margin-bottom:11px}

  .services-band{left:0;top:369px;width:206px;height:38px;background:var(--forest)}
  .services-title{left:41px;top:377px;height:23px;border-left:2px solid var(--white);padding-left:14px;color:var(--white);line-height:23px}
  .icon-globe{left:525px;top:368px;width:27px;height:24px}

  .services{left:41px;top:441px;width:514px}
  .service h3{font-family:"Ubuntu",sans-serif;font-size:10px;font-weight:500;color:var(--leaf);margin-bottom:5px}
  .service p{font-size:8.3px;line-height:11.2px;text-align:justify;margin-bottom:6px}

  .web-panel{left:607px;top:369px;width:280px;height:179px;background:var(--forest)}
  .web-invite{left:629px;top:396px;width:236px;font-family:"Ubuntu",sans-serif;font-weight:300;font-size:21.5px;line-height:26.5px;color:var(--leaf);text-align:justify;text-align-last:justify}
  .web-address{left:627px;top:489px;font-family:"Ubuntu",sans-serif;font-weight:500;font-size:17.5px;color:var(--white);white-space:nowrap}

  /* clients page */
  .clients-panel{left:911px;top:0;width:289px;height:849px;background:linear-gradient(160deg,var(--navy-light) 0%,var(--navy) 45%,#0b1d2b 100%)}
  .clients-rule{left:1003px;top:0;width:2px;height:74px;background:var(--white)}
  .clients-title{left:1019px;top:50px;color:var(--white);line-height:24px}
  .clients{left:955px;top:100px;width:215px;color:#e6ecef}
  .client h3{font-family:"Ubuntu",sans-serif;font-size:10px;font-weight:700;color:var(--leaf);margin-bottom:12px}
  .client p{font-size:8.3px;line-height:11.2px;text-align:justify;margin-bottom:28px}
  .clients-statement{left:955px;top:520px;width:215px;font-family:"Ubuntu",sans-serif;font-weight:300;font-size:22px;line-height:28.5px;color:var(--leaf)}
  .icon-leaf{left:1120px;top:700px;width:28px;height:28px}
  .brand-name{left:955px;top:754px;width:215px;text-align:center;font-family:"Ubuntu",sans-serif;font-weight:500;font-size:19px;letter-spacing:2px;color:var(--white)}
  .brand-url{left:955px;top:817px;width:215px;text-align:center;font-size:8px;color:var(--white)}
</style>
</head>
<body>
<main class="spread">

  <!-- left page -->
  <div class="abs photo-field" role="img" aria-label="Photo of a red tractor working a dark tilled field under a cloudy sky"></div>
  <dl class="abs caption caption-field">
    <dt>TOP</dt><dd>: Agricultural, oil &amp; gas investigation.</dd>
    <dt>TOP LEFT</dt><dd>: Site remediation &amp; closure.</dd>
    <dt>BOTTOM LEFT</dt><dd>: Riparian restoration &amp; reclamation.</dd>
  </dl>

  <h2 class="abs section-title values-title">OUR VALUES</h2>
  <svg class="abs icon-sprout" viewBox="0 0 26 27" aria-hidden="true">
    <path d="M13 15 C13 8 8 3 2 3 C2 10 7 15 13 15Z" fill="var(--forest)"/>
    <path d="M13 15 C13 8 18 3 24 3 C24 10 19 15 13 15Z" fill="var(--forest)"/>
    <rect x="12" y="13" width="2" height="8" fill="var(--forest)"/>
    <path d="M3 27 C3 21 8 19 13 19 C18 19 23 21 23 27Z" fill="var(--forest)"/>
  </svg>
  <p class="abs values-quote">“We Incorporate Creativity, Practicality And Problem Solving Into All Of Our Projects.”</p>

  <section class="abs mission">
    <h2>OUR MISSION IS SIMPLE.</h2>
    <p>To serve our clients;</p>
    <p>To provide expert and innovative consulting; and</p>
    <p>To deliver cost efficient environmental and regulatory solutions.</p>
  </section>

  <div class="abs values-body">
    <p>Our clients are phenomenal. Client relationships are the foundation of our group. We build our business on our clients’ success. Keystrel prides itself for its ability to listen to our clients’ needs, understand their issues, and present viable solutions.</p>
    <p>Our team is exceptional. Our team focuses on foundational skills. We incorporate creativity, practicality, and problem solving into all of our projects. Our value lies in relationships and our ability to face challenges and work together to effectively deliver exceptional project results.</p>
    <p>Our results are remarkable. We routinely develop and apply the site-specific environmental guideline values that are defensible, more suitable, and less stringent compared to the generic Tier 1 “one-fits-all” approach that is often unnecessarily restrictive. Our subject matter experts skillfully use all tools available in the environmental regulations including Tier 2 guidelines, statistical calculations, subsoil values for salinity and hydrocarbons, as well as guidelines for remote sites. Thinking outside the box is our standard approach...it makes sense!</p>
  </div>

  <div class="abs services-band"></div>
  <h2 class="abs section-title services-title">OUR SERVICES</h2>
  <svg class="abs icon-globe" viewBox="0 0 27 24" aria-hidden="true">
    <circle cx="16" cy="9" r="8" fill="none" stroke="var(--forest)" stroke-width="2"/>
    <path d="M12 4 C15 6 13 9 16 10 C18 11 17 14 19 15" fill="none" stroke="var(--forest)" stroke-width="2"/>
    <path d="M1 17 L7 15 C10 14 12 16 15 16 L20 16 C21 16 21 18 20 18 L14 18 L20 19 L25 15 C26 14 27 16 26 17 L20 22 C18 23 15 23 12 22 L7 21 L1 22Z" fill="var(--forest)"/>
  </svg>

  <section class="abs services">
    <article class="service">
      <h3>Phase I and II Environmental Site Assessments (ESAs)</h3>
      <p>Keystrel’s services include completion of Phase I and Phase II ESAs to Canadian Standards Association’s (CSA) requirements to determine the potential of legacy liabilities associated with historical use of a property.</p>
    </article>
    <article class="service">
      <h3>Soil and Groundwater Remediation</h3>
      <p>Our team has over 50 years of combined senior experience in soil and groundwater remediation. Our soil remediation methodologies include in-situ treatment, bioremediation, phytoremediation, and excavation. Groundwater remediation techniques include monitored natural attenuation, mass balance calculations, pump and treat, and recovery and disposal.</p>
    </article>
    <article class="service">
      <h3>Spill Response, Release Reporting, Assessment, and Remediation</h3>
      <p>Our spill response team aims to effectively remediate releases while ensuring protection of environmental receptors and the public. This includes release reporting, initial response and assessment, impact characterization and delineation, Remediation Action Plan (RAP) development, and “Seven-Day Letter” completion.</p>
    </article>
    <article class="service">
      <h3>Land and Regulatory Applications for Pipelines, Facilities, and Wellsites</h3>
      <p>Keystrel provides regulatory support for a variety of applications in the energy industry including Alberta Utilities Commission Applications for power and gas plant exemptions, Environmental Protection and Enhancement Act (EPEA) applications and approvals, Alberta Energy Regulator (AER) Directive 056 Applications for upstream oil and gas activities, and AER Directive 058 applications for waste management licenses and disposal facilities.</p>
    </article>
    <article class="service">
      <h3>Aquatic Assessment and Monitoring and Wetland Evaluations</h3>
      <p>Keystrel personnel have completed numerous aquatic projects including aquatic assessments of proposed watercourse crossings for pipeline alignments, preparation of site-specific best management practices, turbidity monitoring for Horizontal Directional Drilling (HDD) and open-cut activities, Code of Practice (COP) preparations, and Wetland Assessments classification and documentation.</p>
    </article>
    <article class="service">
      <h3>Reclamation, Detailed Site Assessment, and Reclamation Certificate Applications</h3>
      <p>Keystrel has completed numerous upstream oil and gas projects for wellsites, Oil Sands Exploration (OSE) sites, gravel pits, and pipelines. Reclamation projects include light and heavy reclamation, Detailed Site Assessments (DSA) and reclamation certificate application preparation and approvals.</p>
    </article>
  </section>

  <div class="abs fold" aria-hidden="true"></div>

  <!-- middle page -->
  <div class="abs web-panel"></div>
  <p class="abs web-invite">For A Full List Of Our Service Offerings Please Visit Our Website At :</p>
  <p class="abs web-address">keystrelenvironmental.example</p>
  <div class="abs photo-canola" role="img" aria-label="Photo of a sprayer and green tractor crossing a bright yellow canola field with trees behind"></div>
  <dl class="abs caption caption-canola">
    <dt>TOP</dt><dd>: Contamination monitoring &amp; investigation.</dd>
    <dt>TOP LEFT</dt><dd>: Pipeline remediation.</dd>
    <dt>BOTTOM LEFT :</dt><dd>Terrestrial assessment &amp; protection.</dd>
  </dl>

  <!-- right page -->
  <div class="abs clients-panel" role="img" aria-label="Dark navy backdrop with faint wind turbines at dusk"></div>
  <div class="abs clients-rule"></div>
  <h2 class="abs section-title clients-title">OUR CLIENTS</h2>

  <section class="abs clients">
    <article class="client">
      <h3>Upstream Oil and Gas:</h3>
      <p>Environmental stewardship is a principal component of both future and legacy oil and gas projects. Keystrel brings creative, specialized and cost effective environmental solutions to help our clients “Cut Through the Green Tape”. Whether responding to a spill, completing regulatory applications for a pipeline, or evaluating and remediating site contamination, Keystrel strives to provide our clients with the best solution to maximize value and ensure successful project completion.</p>
    </article>
    <article class="client">
      <h3>Commercial:</h3>
      <p>Successful commercial development requires a clear picture of the historical liability and possible environmental impacts that may affect a site. Keystrel utilizes qualified professionals to assess and determine environmental requirements for commercial site success and applies creative assessment and remedial solutions in achieving closure. We work with regulators to mitigate environmental risk while achieving successful development.</p>
    </article>
    <article class="client">
      <h3>Industrial:</h3>
      <p>Environmental sustainability and air, water, and soil monitoring are at the forefront of ongoing industrial operations. Keystrel’s technical specialists provide support in these areas through industrial regulatory permitting and licensing, and monitoring to maintain compliance. We provide timely regulatory and permitting approvals to meet all stakeholder requirements and ensure our clients’ success.</p>
    </article>
  </section>

  <p class="abs clients-statement">We assist our clients in “Cutting Through the Green Tape” to meet their timelines and stakeholder requirements.</p>
  <svg class="abs icon-leaf" viewBox="0 0 28 28" aria-hidden="true">
    <path d="M4 24 C2 14 8 5 25 3 C26 16 18 25 4 24Z" fill="none" stroke="var(--white)" stroke-width="2"/>
    <path d="M4 24 L20 8" stroke="var(--white)" stroke-width="1.6"/>
  </svg>
  <p class="abs brand-name">KEYSTREL</p>
  <p class="abs brand-url">www.keystrelenvironmental.example</p>

</main>
</body>
</html>
```